Digital Marketing company needs business cards

We are a digital marketing company providing SEO, Bidlinks and Web Development services in Australia and New Zealand. Colours and icons have to match the current website (korvalane.com.au). We'd like to keep the cards simple and clean, using the artwork we have as the background of the slider of the website (the triangles). The card should have horizontal layout.
If we could have our core services on the reverse side that'd be great:
SEO
BidLinks
Web Design&Development
Target Market(s)
Medium size to large businesses
Industry/Entity Type
Digital

```html
<!DOCTYPE html>
<html lang="en">
<head>
<meta charset="utf-8">
<title>Korvalane Business Cards</title>
<link href="https://fonts.googleapis.com/css2?family=Open+Sans:wght@400;600&display=swap" rel="stylesheet">
<style>
  :root {
    --backdrop: #ececec;
    --card: #ffffff;
    --ink: #4a4a4a;
    --ink-soft: #6b6b6b;
    --brand-blue: #1b8fc6;
    --brand-blue-deep: #1479ad;
    --tri-blue: #3f9fd0;
    --tri-teal: #5fb3c0;
    --tri-sea: #6fb6a8;
    --tri-lime: #c8dc8e;
    --tri-pale: #bfe0ea;
  }
  * { box-sizing: border-box; margin: 0; padding: 0; }
  html, body {
    width: 1200px;
    height: 900px;
    overflow: hidden;
    background: var(--backdrop);
    font-family: "Open Sans", Arial, sans-serif;
  }
  .canvas {
    position: relative;
    width: 1200px;
    height: 900px;
  }
  .card {
    position: absolute;
    top: 296px;
    width: 540px;
    height: 309px;
    background: var(--card);
    overflow: hidden;
    box-shadow: 0 6px 18px rgba(0,0,0,0.12);
  }
  .card--front { left: 40px; }
  .card--back { left: 620px; }

  .brand {
    position: absolute;
    display: flex;
    align-items: center;
    gap: 10px;
    font-weight: 600;
    font-size: 38px;
    letter-spacing: -0.5px;
    color: var(--brand-blue);
    line-height: 1;
  }
  .brand__dot {
    width: 30px;
    height: 30px;
    border-radius: 50%;
    background: var(--brand-blue);
  }
  .card--front .brand { top: 44px; left: 150px; }

  .address {
    position: absolute;
    top: 112px;
    left: 30px;
    font-size: 12.5px;
    line-height: 1.45;
    color: var(--ink-soft);
  }

  .contact {
    position: absolute;
    top: 140px;
    left: 290px;
  }
  .contact__name {
    font-size: 19px;
    color: var(--ink);
    line-height: 1.2;
  }
  .contact__role {
    font-size: 12px;
    color: var(--ink-soft);
    margin-bottom: 10px;
  }
  .contact__list {
    list-style: none;
    font-size: 12.5px;
    line-height: 1.45;
    color: var(--ink);
  }
  .contact__key {
    display: inline-block;
    width: 16px;
    color: var(--brand-blue);
  }

  .services {
    position: absolute;
    left: 0;
    right: 0;
    bottom: 0;
    height: 42px;
    background: linear-gradient(90deg, var(--brand-blue-deep), var(--brand-blue));
    color: #ffffff;
    font-size: 13px;
    display: flex;
    align-items: center;
    padding-left: 60px;
    letter-spacing: 0.2px;
  }

  .pattern {
    position: absolute;
    inset: 0;
    background:
      linear-gradient(160deg, var(--tri-pale) 0%, rgba(191,224,234,0) 40%),
      linear-gradient(135deg, #2f6fb3 0%, var(--tri-blue) 30%, var(--tri-teal) 58%, var(--tri-sea) 78%, var(--tri-lime) 100%);
  }
  .card--back .brand { top: 132px; left: 70px; color: #3d4a55; }
  .card--back .brand__dot { background: #3d4a55; }
</style>
</head>
<body>
<main class="canvas">
  <section class="card card--front" aria-label="Business card front">
    <div class="brand">korvalane<span class="brand__dot"></span></div>
    <address class="address" style="font-style:normal">
      Level 3, Unit 8 Harbour Yard<br>
      14 Wattle Lane<br>
      Redmond Hill, QLD 4102
    </address>
    <div class="contact">
      <p class="contact__name">Marcus Elwood</p>
      <p class="contact__role">managing director</p>
      <ul class="contact__list">
        <li><span class="contact__key">M</span>0400 123 456</li>
        <li><span class="contact__key">P</span>07 3100 2200</li>
        <li><span class="contact__key">E</span>melwood@korvalane.com.au</li>
        <li><span class="contact__key">W</span>www.korvalane.com.au</li>
      </ul>
    </div>
    <div class="services">SEO &bull; BidLinks &bull; Web Design &amp; Development</div>
  </section>

  <section class="card card--back" aria-label="Business card back">
    <div class="pattern" role="img" aria-label="Faceted triangle pattern in blues, teals and soft greens"></div>
    <div class="brand">korvalane<span class="brand__dot"></span></div>
  </section>
</main>
</body>
</html>
```